Looking for a high-end business card design for a construction company

We are looking to update our business card design. We are a post-frame construction company that builds custom buildings, commercial spaces, homes, and anything else. We have multiple people working here so we would need something we can easily customize the information for the specific person. We need a name, website, cell phone, office phone as well as social icons. Our colors are black, white, and grey/silver so I would love a black background or something that is more striking than just a traditional white business card. Looking for something that is very professional with a high-end look/feel. I have attached our logos, they can be silver, white, grey, or black.
Industry/Entity Type
Construction
Contact Information for Business Card
Business logo, Name, Cell phone, Office phone, website, social Icons
Colors
Designer to choose only greyscale colors for use in the design.
Look and feel

```html
<!DOCTYPE html>
<html lang="en">
<head>
<meta charset="utf-8">
<title>Hartwell Builders – Business Cards</title>
<link href="https://fonts.googleapis.com/css2?family=Montserrat:wght@400;600;800&display=swap" rel="stylesheet">
<style>
  :root {
    --backdrop: #2a2a2a;
    --card: #ffffff;
    --ink: #111111;
    --ink-soft: #333333;
    --silver: #9a9a9a;
  }
  * { box-sizing: border-box; margin: 0; padding: 0; }
  html, body { width: 1200px; height: 960px; overflow: hidden; }
  body {
    background: var(--backdrop);
    font-family: "Montserrat", sans-serif;
    color: var(--ink);
    display: flex;
    flex-direction: column;
    align-items: center;
    justify-content: center;
    gap: 60px;
  }
  .card {
    position: relative;
    width: 700px;
    height: 400px;
    background: var(--card);
    border-radius: 26px;
    overflow: hidden;
  }
  .brand {
    display: flex;
    align-items: center;
    gap: 16px;
  }
  .brand-dot {
    width: 58px; height: 58px;
    border-radius: 50%;
    background: var(--ink);
  }
  .brand-name {
    font-weight: 800;
    font-size: 30px;
    line-height: 1.05;
    letter-spacing: 2px;
    text-transform: uppercase;
    color: var(--ink);
  }
  .card-front .brand {
    position: absolute;
    left: 50%; top: 50%;
    transform: translate(-50%, -50%);
  }
  .card-back .brand {
    position: absolute;
    left: 60px; top: 46px;
  }
  .card-back .brand-dot { width: 50px; height: 50px; }
  .card-back .brand-name { font-size: 26px; }
  .wave { position: absolute; inset: 0; }
  .person {
    position: absolute;
    left: 60px; top: 168px;
  }
  .person-name {
    font-weight: 800;
    font-size: 24px;
    letter-spacing: 0.5px;
    text-transform: uppercase;
  }
  .person-title {
    font-size: 15px;
    color: var(--ink-soft);
    margin-top: 4px;
  }
  .divider {
    position: absolute;
    left: 340px; top: 130px;
    width: 2px; height: 110px;
    background: var(--ink);
  }
  .contacts {
    position: absolute;
    left: 364px; top: 128px;
    list-style: none;
  }
  .contacts li {
    display: flex;
    align-items: center;
    gap: 10px;
    font-size: 17px;
    height: 38px;
  }
  .contacts svg { width: 18px; height: 18px; fill: var(--ink); }
  .address {
    position: absolute;
    left: 90px; top: 262px;
    font-size: 17px;
  }
</style>
</head>
<body>
  <section class="card card-front">
    <div class="brand">
      <span class="brand-dot"></span>
      <span class="brand-name">Hartwell<br>Builders, Inc.</span>
    </div>
  </section>

  <section class="card card-back">
    <svg class="wave" viewBox="0 0 700 400" aria-hidden="true">
      <path d="M700,268 C600,273 560,328 430,352 C330,372 180,388 40,398" fill="none" stroke="var(--silver)" stroke-width="6"/>
      <path d="M700,284 C605,289 565,343 440,366 C340,384 190,396 60,400 L700,400 Z" fill="var(--ink)"/>
    </svg>

    <div class="brand">
      <span class="brand-dot"></span>
      <span class="brand-name">Hartwell<br>Builders, Inc.</span>
    </div>

    <div class="person">
      <div class="person-name">Martin Caldwell</div>
      <div class="person-title">Director of Business Development</div>
    </div>

    <div class="divider"></div>

    <ul class="contacts">
      <li>
        <svg viewBox="0 0 24 24"><path d="M6.6 10.8a15.1 15.1 0 0 0 6.6 6.6l2.2-2.2a1 1 0 0 1 1-.25 11.4 11.4 0 0 0 3.6.57 1 1 0 0 1 1 1V20a1 1 0 0 1-1 1A17 17 0 0 1 3 4a1 1 0 0 1 1-1h3.5a1 1 0 0 1 1 1c0 1.25.2 2.45.57 3.6a1 1 0 0 1-.25 1z"/></svg>
        555 210 4830
      </li>
      <li>
        <svg viewBox="0 0 24 24"><path d="M3 7c0-2 4-4 9-4s9 2 9 4v2h-4V7.5c-1.5-.6-3-.9-5-.9s-3.5.3-5 .9V9H3z"/><rect x="5" y="11" width="14" height="10" rx="2"/></svg>
        555-318-2749
      </li>
      <li>
        <svg viewBox="0 0 24 24"><circle cx="12" cy="12" r="10"/><path d="M2 12h20M12 2c3 3 3 17 0 20M12 2c-3 3-3 17 0 20" stroke="#fff" stroke-width="1.4" fill="none"/></svg>
        www.hartwellbuild.com
      </li>
    </ul>

    <p class="address">2870 Ridge Road Suite 410 Oakvale, CA 900</p>
  </section>
</body>
</html>
```